Wobble Tin Circle - New Website Design

Create a professional Shopify website for a the hottest trend; a slime subscription box business. Storvanta.com is an easy to use website builder.
Please see http://pellowhub.com and zinterpak.com for the concept I am after. The business has not been launched yet, I am currently in the pre-launch stage using a specialized landing page website, and so the time scale for developing my professional looking Shopify website is up to 1-2 weeks.
The webpage should have a fun feel and should match the style of the company logo at pellowhub.com. The pages to include are 'Home', 'About us' and 'Get Started'
Thank you and good luck!
Business
Coded - Design and coding required
1 page

```html
<!DOCTYPE html>
<html lang="en">
<head>
<meta charset="utf-8">
<title>Wobble Tin Circle</title>
<link href="https://fonts.googleapis.com/css2?family=Montserrat:wght@400;500;600;700;800&family=Open+Sans:wght@400;600&display=swap" rel="stylesheet">
<style>
:root{
  --green:#7cc424;
  --green-dark:#5f9e18;
  --ink:#333;
  --text:#555;
  --light:#efefef;
  --white:#fff;
  --footer:#1d1d1d;
  --btn-dark:#4a4a4a;
}
*{box-sizing:border-box;margin:0;padding:0}
html,body{width:1200px;height:3782px;overflow:hidden}
body{font-family:"Open Sans",Arial,sans-serif;color:var(--text);background:var(--white);position:relative}
h1,h2,h3,h4,.nav a,.btn,.wordmark{font-family:"Montserrat",Arial,sans-serif}
section,header,footer{position:absolute;left:0;width:1200px}

/* wordmark: plain text, single colour and weight */
.wordmark{display:flex;align-items:center;gap:10px;color:var(--green);font-weight:700;font-size:24px;line-height:1;white-space:nowrap}
.wordmark::before{content:"";width:14px;height:14px;background:var(--green);flex:0 0 14px}

/* header */
.site-header{top:0;height:105px;background:var(--white)}
.site-header .wordmark{position:absolute;left:75px;top:40px}
.nav{position:absolute;right:75px;top:47px;display:flex;gap:46px}
.nav a{font-size:13px;font-weight:700;color:var(--ink);text-decoration:none;text-transform:uppercase}
.nav a.active{color:var(--green)}

/* hero */
.hero{top:105px;height:555px;background:linear-gradient(135deg,#c9b8a8 0%,#e8ddd4 45%,#d9cfc6 70%,#bdb2a8 100%);text-align:center;color:var(--white)}
.hero-photo{position:absolute;inset:0}
.hero-content{position:absolute;left:0;right:0;top:225px}
.hero h1{font-size:44px;font-weight:800;letter-spacing:.5px;text-shadow:0 1px 4px rgba(0,0,0,.25)}
.hero p{font-family:"Montserrat",sans-serif;font-weight:700;font-size:24px;line-height:32px;margin-top:8px;text-shadow:0 1px 4px rgba(0,0,0,.3)}
.btn{display:inline-block;font-size:13px;font-weight:700;text-transform:uppercase;text-decoration:none;letter-spacing:.5px}
.btn-green{background:var(--green);color:var(--white);padding:13px 40px}
.hero .btn{margin-top:20px}

/* about */
.about{top:660px;height:488px;background:linear-gradient(120deg,#a6e03a,#8fd42a 50%,#b4e85a);text-align:center;color:var(--white)}
.about-content{position:absolute;left:0;right:0;top:155px}
.about h2{font-size:36px;font-weight:700}
.about p{font-size:17px;line-height:29px;width:880px;margin:14px auto 0}
.btn-white{background:var(--white);color:var(--ink);padding:14px 62px;margin-top:22px}

/* feature rows */
.photo{position:absolute}
.feature-text{position:absolute;width:500px}
.feature-text h2{font-size:36px;font-weight:700;color:var(--ink);letter-spacing:.5px}
.feature-text p{font-size:14.5px;line-height:25px;color:var(--text);margin-top:16px}
.link{display:inline-block;margin-top:22px;font-family:"Montserrat",sans-serif;font-size:12.5px;font-weight:700;color:var(--green);text-transform:uppercase;text-decoration:none}
.club{top:1148px;height:540px}
.club .photo{left:75px;top:72px;width:512px;height:338px;background:linear-gradient(135deg,#5a4a3e,#c9474a 45%,#e6e2de 75%,#d35a2a)}
.club .feature-text{left:630px;top:140px}
.inside{top:1688px;height:417px}
.inside .photo{left:615px;top:0;width:510px;height:342px;background:linear-gradient(140deg,#d2b894,#9c6f52 45%,#5ab4d6 70%,#e8e0d4)}
.inside .feature-text{left:78px;top:75px}

/* testimonials */
.testimonials{top:2105px;height:350px;background:var(--light)}
.section-title{font-family:"Montserrat",sans-serif;font-size:21px;font-weight:700;color:var(--ink);text-align:center;text-transform:uppercase;letter-spacing:.5px}
.testimonials .section-title{position:absolute;left:0;right:0;top:50px}
.quote{position:absolute;top:118px;width:480px;display:flex;gap:28px}
.quote-left{left:75px}
.quote-right{left:615px}
.avatar{flex:0 0 88px;height:88px;border-radius:50%;background:linear-gradient(135deg,#bfe3f2,#4fb9e0)}
.quote-right .avatar{background:linear-gradient(135deg,#d8cfc4,#8a7b6e)}
.quote blockquote{font-size:14.5px;line-height:27px;color:var(--text)}
.quote cite{display:block;margin-top:14px;font-style:normal;font-family:"Montserrat",sans-serif;font-size:12px;font-weight:700;color:var(--green);text-transform:uppercase}

/* get started */
.start{top:2455px;height:480px}
.start .photo{left:75px;top:70px;width:515px;height:330px;background:radial-gradient(ellipse at 55% 45%,#f7b6d6 0%,#ec8fbf 35%,#f4eef2 70%,#fff 100%)}
.start .feature-text{left:630px;top:135px}
.start .btn-green{margin-top:20px;padding:13px 22px}

/* gallery */
.gallery{top:2935px;height:315px;background:var(--light)}
.gallery .section-title{position:absolute;left:0;right:0;top:50px}
.thumbs{position:absolute;left:75px;top:105px;display:flex;gap:21px}
.thumb{width:158px;height:135px}
.thumb:nth-child(1){background:linear-gradient(135deg,#e6c7b4,#5ab7d8)}
.thumb:nth-child(2){background:linear-gradient(135deg,#d9b69c,#f0a830)}
.thumb:nth-child(3){background:linear-gradient(135deg,#a8c36a,#e2c9b0)}
.thumb:nth-child(4){background:linear-gradient(135deg,#c9a08a,#e9e4e0)}
.thumb:nth-child(5){background:linear-gradient(135deg,#6b4e3d,#7ad24a)}
.thumb:nth-child(6){background:linear-gradient(135deg,#5fc0b0,#d4b8a8)}

/* newsletter */
.newsletter{top:3250px;height:245px;background:var(--green);text-align:center;color:var(--white)}
.newsletter h3{position:absolute;left:0;right:0;top:52px;font-size:20px;font-weight:700;text-transform:uppercase}
.newsletter p{position:absolute;left:0;right:0;top:86px;font-size:14.5px}
.signup{position:absolute;left:253px;top:130px;display:flex;gap:15px}
.signup .field{width:512px;height:52px;background:var(--white);color:var(--ink);font-size:13px;text-align:left;padding:17px 20px;font-family:"Montserrat",sans-serif;font-weight:500}
.signup .btn{background:var(--btn-dark);color:var(--white);width:168px;height:52px;line-height:52px;padding:0}

/* footer */
.site-footer{top:3495px;height:287px;background:var(--footer);color:var(--white)}
.foot-col{position:absolute;top:52px}
.foot-col h4{font-size:14px;font-weight:700;text-transform:uppercase;margin-bottom:12px}
.foot-col a{display:block;font-size:13px;line-height:29px;color:var(--green);text-decoration:none}
.col-nav{left:75px}.col-service{left:343px}.col-social{left:628px}
.col-social a{display:flex;align-items:center;gap:14px}
.col-social a::before{content:"";width:7px;height:7px;background:var(--green)}
.site-footer .wordmark{position:absolute;left:900px;top:100px;width:240px;justify-content:center;font-size:22px}
.copyright{position:absolute;left:900px;top:160px;width:240px;text-align:center;font-size:13px;line-height:21px;color:#cfcfcf}
</style>
</head>
<body>

<header class="site-header">
  <div class="wordmark">Wobble Tin Circle</div>
  <nav class="nav">
    <a class="active" href="#">Home</a>
    <a href="#">About Us</a>
    <a href="#">Get Started</a>
    <a href="#">Slime Club</a>
    <a href="#">Contact Us</a>
  </nav>
</header>

<section class="hero">
  <div class="hero-photo" role="img" aria-label="Child holding up colourful blue and orange slime in both hands"></div>
  <div class="hero-content">
    <h1>WOBBLE TIN CIRCLE</h1>
    <p>Vestibulum ante ipsum primis in faucibus<br>orci luctus et ultrices posuere cubilia</p>
    <a class="btn btn-green" href="#">Get Started</a>
  </div>
</section>

<section class="about" role="img" aria-label="Green slime stretched between hands under a lime tint">
  <div class="about-content">
    <h2>ABOUT WOBBLE TIN CIRCLE</h2>
    <p>Suspendisse lobortis turpis in odio blandit ac interdum lorem euismod risus massa, vulputate eu pellentesque et, consectetur a neque.</p>
    <a class="btn btn-white" href="#">Read More</a>
  </div>
</section>

<section class="club">
  <div class="photo" role="img" aria-label="Two children making red slime at a table"></div>
  <div class="feature-text">
    <h2>SLIME CLUB</h2>
    <p>Aliquam molestie, mi et imperdiet euismod, dui purus auctor tellus, et interdum lacus lectus et ante. Sed accumsan sollicitudin sapien, sit amet adipiscing turpis gravida ac.</p>
    <a class="link" href="#">Read More</a>
  </div>
</section>

<section class="inside">
  <div class="feature-text">
    <h2>WHAT INSIDE THE BOX</h2>
    <p>Aliquam molestie, mi et imperdiet euismod, dui purus auctor tellus, et interdum lacus lectus et ante. Sed accumsan sollicitudin sapien, sit amet adipiscing turpis gravida ac.</p>
    <a class="link" href="#">Read More</a>
  </div>
  <div class="photo" role="img" aria-label="Child mixing blue slime with craft supplies on a wooden floor, seen from above"></div>
</section>

<section class="testimonials">
  <h3 class="section-title">Testimonials</h3>
  <div class="quote quote-left">
    <div class="avatar" role="img" aria-label="Customer portrait"></div>
    <div>
      <blockquote>“ Aliquam molestie, mi et imperdiet euismod, dui purus auctor tellus, et interdum lacus lectus et ante. Sed accumsan sollicitudin sapien, sit amet adipiscing turpis gravida ac lobortis turpis in odio blandit ac interdum lorem euismod..”</blockquote>
      <cite>-Name Heading</cite>
    </div>
  </div>
  <div class="quote quote-right">
    <div class="avatar" role="img" aria-label="Customer portrait"></div>
    <div>
      <blockquote>“ Aliquam molestie, mi et imperdiet euismod, dui purus auctor tellus, et interdum lacus lectus et ante. Sed accumsan sollicitudin sapien, sit amet adipiscing turpis gravida ac lobortis turpis in odio blandit ac interdum lorem euismod..”</blockquote>
      <cite>-Name Heading</cite>
    </div>
  </div>
</section>

<section class="start">
  <div class="photo" role="img" aria-label="Tub of pink slime spilling out beside small slime pots"></div>
  <div class="feature-text">
    <h2>GET STARTED</h2>
    <p>Aliquam molestie, mi et imperdiet euismod, dui purus auctor tellus, et interdum lacus lectus et ante. Sed accumsan sollicitudin sapien, sit amet adipiscing turpis gravida ac.</p>
    <a class="btn btn-green" href="#">Get Started Now</a>
  </div>
</section>

<section class="gallery">
  <h3 class="section-title">Follow Us On Snapgallery</h3>
  <div class="thumbs">
    <div class="thumb" role="img" aria-label="Hands pressing blue slime"></div>
    <div class="thumb" role="img" aria-label="Child stretching orange slime"></div>
    <div class="thumb" role="img" aria-label="Children playing with slime outdoors"></div>
    <div class="thumb" role="img" aria-label="Hands pulling clear slime"></div>
    <div class="thumb" role="img" aria-label="Child holding green slime"></div>
    <div class="thumb" role="img" aria-label="Teal slime stretched between hands"></div>
  </div>
</section>

<section class="newsletter">
  <h3>Keep In Touch!</h3>
  <p>Use this section to let customers sign up for your store newsletter.</p>
  <div class="signup">
    <div class="field">Enter Your Email</div>
    <a class="btn" href="#">Subscribe</a>
  </div>
</section>

<footer class="site-footer">
  <div class="foot-col col-nav">
    <h4>Navigation</h4>
    <a href="#">Home</a><a href="#">About us</a><a href="#">Get started</a><a href="#">Slime Club</a><a href="#">Contact us</a>
  </div>
  <div class="foot-col col-service">
    <h4>Customer Service</h4>
    <a href="#">FAQs</a><a href="#">Account</a><a href="#">Contact</a><a href="#">Terms &amp; Conditions</a><a href="#">Privacy Policy</a>
  </div>
  <div class="foot-col col-social">
    <h4>Find Us Online</h4>
    <a href="#">Friendwall</a><a href="#">Chirpline</a><a href="#">Pinboardly</a><a href="#">Snapgallery</a>
  </div>
  <div class="wordmark">Wobble Tin Circle</div>
  <p class="copyright">Copyright © 2017 Company Name<br>All Rights Reserved</p>
</footer>

</body>
</html>
```